Event Listing Website

We need a redesign of a site for a new startup that lists local events such as concerts, night clubs, stand up comedy shows, theater plays, festivals, conferences, seminars, and family events.

The original design was done by programmers, not designers, and thus can be greatly improved, especially in terms of flow and usability.

The current site can be viewed at:
http://projects.brightmesharbor.com/pavlento/index.php/events/

The successful designer may also be hired for additional work. In fact, we are looking for a long-time partner that may eventually fill a Creative Director role with this new venture..

Things to note:

The site should not look like a nightlife/disco/club site since the site lists events from concerts to conferences to family events.

There is a lot of content on the site, thus it needs to be clean, easy to read and navigate.

Our mission is to have a “Unique” site, that stands out from the traditional ones

Currently the site has these main sections:

Homepage
Events
Venues
Cinema

These sections have the following content types or page layouts:

Homepage
Listing of events
Listing of venues
Event details
Venue details
Cinema summary page
Film details
Film theater details
Blog/news
Account overview page
Updates

Please note, an important element of the site is the location picker that is currently on the top left of our site (the black drop down button that says "change", enter Velmora for example). The site displays events based on user location, users need to know what city the site is using and need to be able to change such city. This works similar to many sites such as www.dealquarry.com, www.nightpelt.com, and www.happenlo.com.

Also, please note that we would eventually use background ads on the homepage. See www.reelwick.com for example.

I have extended the project further. Thanks!

Please note, after the main menu (Home, Events, Venues, Cinema) these pages or features are very important and should be visible and prominent. We currently have them on a bar across the top that remains fixed as you scroll down, but it may not be the best location, so we look forward to some fresh ideas. Thanks.

In order of importance:

1. Change your location (Button that says current city with option to change it)
2. Add event (link)
3. Add venue (link)
4. Login (link)
5. Change language (drop down button with languages)

I just increased the budget by $40 :)

When submitting a design, please submit two versions, one with background advertisement, and one without. This way we can see if there are too many colors or distractions.

Here is a sample background advertisement to use: http://lentobanner.cloudvault-example.com/img_uploads/72/77_191072_3_Korvex_Lyra_Tab_Adspire_newsbit_skin2.jpg

Hello all, thanks for submitting your beautiful designs. It has made our decision very difficult. We decided to award to project to Pembrio, who is currently working on making some tweaks to his submission. Thus are no longer accepting designs. Thanks again.

Target Market(s)

17-40 year olds, male and female, clubbers, concert goers, professionals, athletes, families, and kids

Industry/Entity Type

Events

Requirements
Must have
• Needs to follow Brevlin grid system. See http://brevlin.gx.
Nice to have
• We like the colors Tarvik Nearby
(http://nearby.tarvik.com/westside-south-bay)

We like Dealquarry theme as well
(http://www.dealquarry.com/los-angeles/)

Happenlo is a site similar to ours, we like the overall layout and how easy it is to navigate, not necessarily the colors though:
(http://happenlo.com/)
Should not have
• The site should not look like a nightlife/disco/club site.

Besides clubs, the site lists events from concerts to conferences to family events.

Should definitely not use serif fonts such as Times New Roman

```html
<!DOCTYPE html>
<html lang="it">
<head>
<meta charset="utf-8">
<title>Pavlento – Eventi</title>
<link href="https://fonts.googleapis.com/css2?family=Arimo:ital,wght@0,400;0,700;1,400;1,700&display=swap" rel="stylesheet">
<style>
:root{
  --bg:#e4e4e4;
  --page:#ffffff;
  --ink:#222222;
  --muted:#555555;
  --blue:#4f7fb4;
  --blue-dark:#3d6797;
  --link:#2f63a8;
  --orange:#f28a1c;
  --line:#d5d5d5;
  --panel:#f2f2f2;
  --footer:#3b3b3b;
  --footer-text:#dddddd;
}
*{box-sizing:border-box;margin:0;padding:0}
html,body{width:861px;height:1200px;overflow:hidden}
body{background:var(--bg);font-family:"Arimo",Arial,sans-serif;color:var(--ink);position:relative}
.page{position:absolute;left:135px;top:98px;width:591px;height:1080px;background:var(--page);box-shadow:0 0 6px rgba(0,0,0,.25)}
.abs{position:absolute}

/* header */
.brand{left:20px;top:12px;font-size:40px;font-weight:700;color:#333;letter-spacing:-.5px}
.tagline{left:200px;top:30px;font-size:11px;font-style:italic;color:var(--link);line-height:14px;text-align:center;width:150px}
.top-links{right:14px;top:8px;display:flex;gap:9px;font-size:9.5px}
.top-links a{color:#222;text-decoration:none}
.social{right:14px;top:56px;display:flex;gap:4px}
.social span{width:13px;height:13px;border-radius:2px;display:block}

/* nav */
.nav{left:0;top:78px;width:591px;height:24px;background:linear-gradient(#5b8cc2,var(--blue-dark));display:flex;align-items:center}
.nav a{color:#fff;font-size:9.5px;text-decoration:none;padding:0 14px;height:24px;line-height:24px;border-right:1px solid #6e98c6}
.search{right:14px;top:83px;display:flex;gap:4px}
.search .field{width:90px;height:14px;background:#fff;font-size:8px;padding:2px 3px;color:#333}
.search .btn{width:55px;height:14px;background:var(--orange);color:#fff;font-size:8.5px;text-align:center;line-height:14px;border-radius:2px}

/* boxes */
.box{border:1px solid var(--line);background:#fff}
.box-head{height:24px;background:linear-gradient(#5a8ac0,var(--blue-dark));color:#fff;font-size:11px;font-weight:700;padding:6px 10px}
.featured{left:12px;top:117px;width:351px;height:178px;background:var(--panel)}
.featured .inner{position:absolute;left:6px;top:30px;right:6px;bottom:6px;background:#fff;border:1px solid var(--line)}
.photo{left:13px;top:16px;width:84px;height:98px;border:1px solid #bbb;background:linear-gradient(#d7c3ae,#8a6f58)}
.event-name{left:106px;top:17px;width:226px;height:22px;background:#eee;border:1px solid #ddd;font-size:12px;font-weight:700;color:var(--link);padding:4px 8px}
.event-info{left:106px;top:46px;font-size:8px;line-height:10px}
.event-info b{display:block}
.btn-orange{background:var(--orange);color:#fff;font-size:8.5px;text-align:center;border-radius:2px}
.buy{left:111px;top:112px;width:62px;height:18px;line-height:18px}

.map-box{left:375px;top:117px;width:204px;height:178px;background:var(--panel)}
.map{left:7px;top:7px;width:188px;height:148px;background:linear-gradient(135deg,#c6dcef,#e8e4d6 55%,#cfe0b8)}
.map-btn{right:7px;top:159px;width:74px;height:15px;line-height:15px}

.rail{left:12px;width:351px;height:135px}
.rail-title{height:22px;font-size:11px;color:var(--link);padding:5px 6px;border-bottom:1px solid var(--line)}
.strip{position:absolute;left:0;right:0;top:22px;bottom:0;background:linear-gradient(#eeeeee,#ffffff 40%)}
.arrow{position:absolute;top:22px;width:23px;height:45px;background:#fff;border:1px solid #ccc;border-radius:4px}
.arrow svg{position:absolute;left:6px;top:15px}
.thumb{position:absolute;top:12px;width:60px;text-align:center;font-size:7.5px;line-height:9px;color:#333}
.thumb .pic{width:60px;height:57px;border:2px solid #fff;box-shadow:0 1px 3px rgba(0,0,0,.45);margin-bottom:6px}

.newsletter{left:12px;top:752px;width:351px;height:115px;background:var(--blue);padding:9px 8px}
.newsletter h2{font-size:14px;color:#fff;font-weight:700}
.newsletter .field{position:absolute;left:8px;top:42px;width:273px;height:22px;background:#fff}
.newsletter .btn-orange{position:absolute;left:288px;top:42px;width:56px;height:22px;line-height:22px;font-size:10px}

.social-box{left:375px;top:310px;width:204px;height:395px;background:var(--panel)}
.social-inner{left:6px;top:6px;width:190px;height:380px;background:#fff;border:1px solid #ccc;font-size:7px;color:#333}
.social-inner .bar{background:#eee;border-bottom:1px solid #ccc;padding:4px 6px;font-weight:700;font-size:7.5px}
.page-id{left:8px;top:22px;display:flex;gap:5px}
.page-id .logo{width:20px;height:20px;border:1px solid #ccc;background:#f4f4f4}
.page-id .name{color:var(--link);font-weight:700;font-size:8px}
.like{display:inline-block;border:1px solid #aab;font-size:6.5px;padding:1px 4px;margin-top:2px;background:#eef}
.stream{left:6px;top:50px;width:176px;height:180px;border:1px solid #ccc;overflow:hidden}
.post{position:relative;padding:6px 4px 6px 32px;border-bottom:1px solid #e3e3e3;line-height:9px;height:88px}
.post .av{position:absolute;left:4px;top:8px;width:22px;height:22px;border:1px solid #ccc;background:#f4f4f4}
.post b{color:var(--link);display:block}
.post i{color:#999;font-style:normal}
.fans{left:6px;top:240px;font-size:7px}
.fan-row{left:6px;top:255px;display:flex;gap:7px}
.fan{width:32px;text-align:center;font-size:6px;color:#555}
.fan .pic{width:32px;height:32px;margin-bottom:2px}
.plugin{left:0;bottom:0;width:188px;border-top:1px solid #ccc;padding:3px 6px;font-size:6.5px;color:#555}

.news{left:375px;top:715px;width:204px;height:162px;background:#fff}
.news-head{height:22px;background:linear-gradient(#f4f4f4,#dcdcdc);font-size:12px;font-weight:700;color:#444;padding:4px 8px;border-bottom:1px solid var(--line)}
.news-item{padding:3px 8px 5px;font-size:7.5px;line-height:9px;border-bottom:1px solid #eee}
.news-item .date{color:var(--orange);font-weight:700;margin-bottom:3px}
.news-item p{padding-left:16px;color:#333}
.news-item.alt{background:#f3f3f3}

.footer{left:0;top:887px;width:591px;height:193px;background:var(--footer)}
.footer-nav{position:absolute;left:0;right:0;top:13px;display:flex;justify-content:space-around;font-size:9px;font-weight:700;color:#fff}
.footer-list{position:absolute;left:255px;top:43px;font-size:8.5px;line-height:10.5px;color:#bbb;list-style:none}
.footer-rule{position:absolute;left:10px;right:10px;top:150px;border-top:1px solid #555}
.copyright{position:absolute;left:0;right:0;top:166px;text-align:center;font-size:8px;color:#ccc}
</style>
</head>
<body>
<div class="page">

  <header>
    <div class="abs brand">Pavlento</div>
    <div class="abs tagline">Lorem Ipsum Dolor Sit Amet Consectetur Adipiscing</div>
    <nav class="abs top-links"><a href="#">Home</a><a href="#">FAQ's</a><a href="#">Register</a><a href="#">Login</a><a href="#">Contact Us</a></nav>
    <div class="abs social" aria-label="Social links">
      <span style="background:#39a9d9"></span><span style="background:#3b5b98"></span><span style="background:#f28a1c"></span><span style="background:#2a78b0"></span>
    </div>
  </header>

  <nav class="abs nav"><a href="#">Home</a><a href="#">Event</a><a href="#">Venues</a><a href="#">Cinema</a></nav>
  <div class="abs search"><div class="field">Keywords</div><div class="btn">Search</div></div>

  <section class="abs box featured">
    <div class="box-head" style="position:absolute;left:6px;right:6px;top:6px">Eventi In Prima Fila</div>
    <div class="inner">
      <div class="abs photo" role="img" aria-label="Portrait photo of the featured performer"></div>
      <div class="abs event-name">Lorenzo Bertali</div>
      <div class="abs event-info">
        <b>Quando</b>2012 – 03 – 04<br>Dove<br>Via Calvetti 8, MELZARO, Italia, 20124<br>MELZARO<br>Italia
      </div>
      <div class="abs btn-orange buy">Buy Tickets</div>
    </div>
  </section>

  <section class="abs box map-box">
    <div class="abs map" role="img" aria-label="Map of Italy showing the event location"></div>
    <div class="abs btn-orange map-btn">View Large Map</div>
  </section>

  <section class="abs box rail" style="top:310px">
    <div class="rail-title">Event Lorem Ipsum Dolor</div>
    <div class="strip">
      <div class="arrow" style="left:10px"><svg width="10" height="14"><path d="M9 1 L1 7 L9 13Z" fill="#333"/></svg></div>
      <div class="thumb" style="left:47px"><div class="pic" role="img" aria-label="Concert photo" style="background:linear-gradient(#c07a86,#4b2a30)"></div>Lorem ipsum dolor sit amet</div>
      <div class="thumb" style="left:113px"><div class="pic" role="img" aria-label="Concert photo" style="background:linear-gradient(#c07a86,#4b2a30)"></div>Lorem ipsum dolor sit amet</div>
      <div class="thumb" style="left:180px"><div class="pic" role="img" aria-label="Concert photo" style="background:linear-gradient(#c07a86,#4b2a30)"></div>Lorem ipsum dolor sit amet</div>
      <div class="thumb" style="left:247px"><div class="pic" role="img" aria-label="Concert photo" style="background:linear-gradient(#c07a86,#4b2a30)"></div>Lorem ipsum dolor sit amet</div>
      <div class="arrow" style="left:317px"><svg width="10" height="14"><path d="M1 1 L9 7 L1 13Z" fill="#333"/></svg></div>
    </div>
  </section>

  <section class="abs box rail" style="top:457px">
    <div class="rail-title">Cinema Lorem Ipsum Dolor</div>
    <div class="strip">
      <div class="arrow" style="left:10px"><svg width="10" height="14"><path d="M9 1 L1 7 L9 13Z" fill="#333"/></svg></div>
      <div class="thumb" style="left:47px"><div class="pic" role="img" aria-label="Film poster" style="background:linear-gradient(#8a7d78,#3a2f2c)"></div>Lorem ipsum dolor sit amet</div>
      <div class="thumb" style="left:113px"><div class="pic" role="img" aria-label="Film poster" style="background:linear-gradient(#a6a07a,#3f3a28)"></div>Lorem ipsum dolor sit amet</div>
      <div class="thumb" style="left:180px"><div class="pic" role="img" aria-label="Film poster" style="background:linear-gradient(#e0b160,#6a4a20)"></div>Lorem ipsum dolor sit amet</div>
      <div class="thumb" style="left:247px"><div class="pic" role="img" aria-label="Film poster" style="background:linear-gradient(#e0b160,#6a4a20)"></div>Lorem ipsum dolor sit amet</div>
      <div class="arrow" style="left:317px"><svg width="10" height="14"><path d="M1 1 L9 7 L1 13Z" fill="#333"/></svg></div>
    </div>
  </section>

  <section class="abs box rail" style="top:604px">
    <div class="rail-title">Venues Lorem Ipsum Dolor</div>
    <div class="strip">
      <div class="arrow" style="left:10px"><svg width="10" height="14"><path d="M9 1 L1 7 L9 13Z" fill="#333"/></svg></div>
      <div class="thumb" style="left:47px"><div class="pic" role="img" aria-label="Venue image" style="background:linear-gradient(#9cc46a,#4f7d2c)"></div>Lorem ipsum dolor sit amet</div>
      <div class="thumb" style="left:113px"><div class="pic" role="img" aria-label="Venue image" style="background:linear-gradient(#9cc46a,#4f7d2c)"></div>Lorem ipsum dolor sit amet</div>
      <div class="thumb" style="left:180px"><div class="pic" role="img" aria-label="Venue image" style="background:linear-gradient(#9cc46a,#4f7d2c)"></div>Lorem ipsum dolor sit amet</div>
      <div class="thumb" style="left:247px"><div class="pic" role="img" aria-label="Venue image" style="background:linear-gradient(#9cc46a,#4f7d2c)"></div>Lorem ipsum dolor sit amet</div>
      <div class="arrow" style="left:317px"><svg width="10" height="14"><path d="M1 1 L9 7 L1 13Z" fill="#333"/></svg></div>
    </div>
  </section>

  <section class="abs newsletter">
    <h2>Ricevere Aggiornamento Settimanale</h2>
    <div class="field"></div>
    <div class="btn-orange">Submit</div>
  </section>

  <aside class="abs box social-box">
    <div class="abs social-inner">
      <div class="bar">Find us on Friendwall</div>
      <div class="abs page-id"><div class="logo"></div><div><div class="name">Pavlento</div><span class="like">Like</span></div></div>
      <div class="abs stream">
        <div class="post"><div class="av"></div><b>Pavlento</b>sed malesuada dolor libero at arcu. Proin ullamcorper imperdiet eleifend. Mauris nec lorem et libero blandit tempor. Nulla facilisi, nunc varius.<br><i>August 5, 2011 at 2:57am</i></div>
        <div class="post"><div class="av"></div><b>Pavlento</b>sed malesuada dolor libero at arcu. Proin ullamcorper imperdiet eleifend. Mauris nec lorem et libero blandit tempor.<br><i>August 5, 2011 at 2:57am</i></div>
      </div>
      <div class="abs fans">4 people like Pavlento.</div>
      <div class="abs fan-row">
        <div class="fan"><div class="pic" role="img" aria-label="Fan avatar" style="background:#8d7a66"></div>Tedo</div>
        <div class="fan"><div class="pic" role="img" aria-label="Fan avatar" style="background:#5a4c44"></div>Tomas</div>
        <div class="fan"><div class="pic" role="img" aria-label="Fan avatar" style="background:#c9cfd8"></div>Fasil</div>
        <div class="fan"><div class="pic" role="img" aria-label="Fan avatar" style="background:#3e82b8"></div>Dewys</div>
      </div>
      <div class="abs plugin">Friendwall social plugin</div>
    </div>
  </aside>

  <aside class="abs box news">
    <div class="news-head">Ultime News</div>
    <div class="news-item"><div class="date">January, 12/2012</div><p>Lorem ipsum dolor sit amet, consectetur adipis dig elit. Set diam nonumy convallis gravida neque</p></div>
    <div class="news-item alt"><div class="date">January, 28/2012</div><p>Lorem ipsum dolor sit amet, consectetur adipis dig elit. Set diam nonumy convallis gravida neque</p></div>
    <div class="news-item"><div class="date">February, 10/2012</div><p>Lorem ipsum dolor sit amet, consectetur adipis dig elit. Set diam nonumy convallis gravida neque</p></div>
  </aside>

  <footer class="abs footer">
    <div class="footer-nav"><span>Home</span><span>Eventi</span><span>Eventi Da Non Perdere</span><span>Categorie Top</span><span>Luoghi Top</span><span>Film Top</span><span>Contact Us</span></div>
    <ul class="footer-list">
      <li>Play</li><li>Altri eventi teatrali</li><li>Mostre d'arte di storia</li><li>Prosa</li><li>Concerts</li><li>Musei e siti archeologici</li>
    </ul>
    <div class="footer-rule"></div>
    <div class="copyright">Copyright © 2011, Pavlento.com. All rights reserved.</div>
  </footer>

</div>
</body>
</html>
```